BRIGHT COLORFUL + 55 FAMILY HISTORY BROCHURE 11 x 17 bifold

11 x 17 Bifold Flyer I have given you the Layout I just need you to make it Pretty

YOU DO NOT NEED TO FOLLOW MY LAYOUT, You can but dont have too

Target Market(s)

55 year old consumers, who could choose our service of Hereditary Cancer Screening

Industry/Entity Type

Health And Wellness

Requirements
Must have
• Must be appealing to Grand Parents, must make them want to test , show lots of pictures of grand children, YOU DO NOT NEED TO FOLLOW MY LAYOUT , You can but dont have too
Nice to have
• use our colors of our logo , YOU DO NOT NEED TO FOLLOW MY LAYOUT , You can but dont have too
Should not have
• YOU DO NOT NEED TO FOLLOW MY LAYOUT, You can but dont have too

```html
<!DOCTYPE html>
<html lang="en">
<head>
<meta charset="utf-8">
<title>Hereditary Cancer Screening – Bifold</title>
<link rel="stylesheet" href="https://fonts.googleapis.com/css2?family=Crimson+Text:wght@400;600;700&family=Comic+Neue:wght@400&family=Tinos:wght@400;700&display=swap">
<style>
  :root{
    --paper:#e2eed3;
    --paper-glow:#edf5e4;
    --navy:#19275c;
    --green:#6cb43c;
    --ink:#1a1a1a;
    --warm-a:#e9d7c6;
    --warm-b:#c99f80;
    --leaf-a:#a9be6a;
    --leaf-b:#5f7d2e;
  }
  *{margin:0;padding:0;box-sizing:border-box}
  html,body{width:1200px;height:782px;overflow:hidden;background:var(--paper)}
  .spread{position:relative;width:1200px;height:782px;background:var(--paper);overflow:hidden;font-family:"Crimson Text",serif;color:var(--navy)}
  .glow{position:absolute;left:380px;top:-110px;width:900px;height:900px;border-radius:50%;background:var(--paper-glow);opacity:.7}
  .photo{position:absolute;background:linear-gradient(135deg,var(--warm-a),var(--warm-b))}
  .photo.outdoor{background:linear-gradient(135deg,var(--leaf-a),var(--warm-b))}
  .photo.hands{background:linear-gradient(120deg,var(--leaf-a),#c7cf86 45%,var(--leaf-b))}
  .center{position:absolute;text-align:center;white-space:nowrap}
  .head{font-weight:700;color:var(--navy)}
  .accent{font-weight:600;color:var(--green)}
  .fine{position:absolute;left:44px;top:669px;font-family:"Tinos",serif;font-size:11.3px;line-height:14px;color:var(--ink);white-space:nowrap}
  .fine b{font-weight:700}
  .brand{position:absolute;top:730px;width:104px;text-align:center;font-family:"Crimson Text",serif;font-weight:600;font-size:19px;color:var(--navy);white-space:nowrap}
  .url{position:absolute;top:746px;font-family:"Crimson Text",serif;font-size:16px;color:var(--green);transform:translateX(-50%);white-space:nowrap}
  .title{position:absolute;left:896px;top:31px;transform:translateX(-50%);font-size:37px;font-weight:700;white-space:nowrap;letter-spacing:.3px}
  .tagline{position:absolute;left:896px;top:79px;transform:translateX(-50%);font-family:"Comic Neue",sans-serif;font-size:25px;white-space:nowrap}
  .grid{position:absolute;left:635px;top:134px;width:522px;height:258px;display:grid;grid-template-columns:repeat(4,1fr);grid-template-rows:repeat(2,1fr);gap:5px}
  .grid .cell{background:linear-gradient(135deg,var(--warm-a),var(--warm-b))}
  .grid .cell.outdoor{background:linear-gradient(135deg,var(--leaf-a),var(--warm-b))}
</style>
</head>
<body>
<main class="spread">
  <div class="glow"></div>

  <!-- Back panel -->
  <div class="photo" style="left:138px;top:44px;width:333px;height:168px" role="img" aria-label="Photo of a grandfather laughing as his granddaughter kisses his cheek, with grandmother beside them"></div>
  <p class="center head" style="left:0;width:610px;top:229px;font-size:22.5px">DOES CANCER <span style="font-weight:600">Run in Your Family?</span></p>
  <p class="center accent" style="left:0;width:610px;top:259px;font-size:19.8px">A Simple Swab <span style="font-weight:400">Could SAVE a Family Member’s LIFE!</span></p>

  <div class="photo outdoor" style="left:138px;top:318px;width:333px;height:168px" role="img" aria-label="Photo of a smiling grandmother receiving kisses from her two grandchildren outdoors"></div>
  <p class="center" style="left:0;width:610px;top:504px;font-size:22.4px;line-height:26.5px;font-weight:600">Your decision won’t just affect you. It will also<br>impact Your Family, since your test results<br>may Forecast Their Cancer Risks, too.</p>
  <p class="center accent" style="left:0;width:610px;top:587px;font-size:19.5px;line-height:23.5px">We believe it is important to understand what can<br>and cannot be learned with genetic testing.</p>

  <p class="fine">Genetic mutations can increase risks for certain cancers, but this does not mean cancer will definitely develop.<br>You should be prepared to receive positive or negative results. <b>Most people receive Negative Results meaning</b><br><b>no mutations associated with an increased risk for Hereditary cancers.</b></p>

  <p class="brand" style="left:462px">Kinward Care</p>
  <p class="url" style="left:254px">www.KinwardScreening.com</p>

  <!-- Front panel -->
  <h1 class="title">Hereditary Cancer Screening</h1>
  <p class="tagline">“The Test You Take For Them”</p>

  <div class="grid">
    <div class="cell" role="img" aria-label="Photo of a grandmother hugging a young granddaughter"></div>
    <div class="cell" role="img" aria-label="Photo of a smiling grandfather receiving a kiss from a grandchild"></div>
    <div class="cell outdoor" role="img" aria-label="Photo of a multigenerational family sitting on the grass"></div>
    <div class="cell" role="img" aria-label="Photo of a grandmother embracing her granddaughter"></div>
    <div class="cell" role="img" aria-label="Photo of a grandfather and granddaughter cheek to cheek"></div>
    <div class="cell outdoor" role="img" aria-label="Photo of a grandfather hugging a small grandson"></div>
    <div class="cell outdoor" role="img" aria-label="Photo of grandparents smiling with a grandchild outdoors"></div>
    <div class="cell" role="img" aria-label="Photo of a grandmother laughing as her granddaughter hugs her"></div>
  </div>

  <p class="center" style="left:600px;width:592px;top:403px;font-size:22.4px;line-height:26.5px;font-weight:600">Will you give your loved ones the information<br>to Beat Cancer in their lives?</p>

  <div class="photo hands" style="left:710px;top:472px;width:333px;height:168px" role="img" aria-label="Photo of a small child’s hand holding an older adult’s finger"></div>

  <p class="center" style="left:600px;width:592px;top:648px;font-size:22px;font-weight:600">Give Them the Gift of Knowledge</p>
  <p class="center accent" style="left:600px;width:592px;top:677px;font-size:19.5px">Knowing is better than not knowing. Knowledge is Power!</p>

  <p class="brand" style="left:635px">Kinward Care</p>
  <p class="url" style="left:946px">www.KinwardScreening.com</p>
</main>
</body>
</html>
```